Vital Harbor Business Card Design

New Business card design for Vital Harbor. Content should be similar to the
current business card. I have attached the new logo below. We are looking for a more modern look for our new business cards.

New Logo (see attachment)
New Address: 27591 Maple Crest Parkway, Mapleview, KS 77592
Larger map on back showing our location covering most of the back side.
I would like a small section on the back near the bottom where it
says 'Membership:_____________________' so we can write promotional info.
Add: IG/FB @VHMapleview to the front side

Target Market(s)

Local Market, Sports enthusiast, vitamin and supplement purchaser.

Industry/Entity Type

Health And Wellness

Contact Information for Business Card

See attached. Card will be glossy finish both front and back except the area
for 'Membership:' information where it can be a matte finish.

Requirements
Must have
• New Logo (see attachment)
• Address: 27591 Maple Crest Parkway, Mapleview, KS 77592
• Larger map on back.
• I would like a small section on the back near the bottom where it
• says 'Membership:_____________________'
• so we can write promotional info.
• Add: IG/FB @VHMapleview
Nice to have
• Our logo consists of colors red, black and white. We can use other colors for background etc.
Should not have
• No need to say 'Next to Colwater's Restaurant (in Pemford's Shopping Center)'
• as this is no longer applicable.

```html
<!DOCTYPE html>
<html lang="en">
<head>
<meta charset="utf-8">
<title>Vital Harbor Business Card</title>
<link rel="stylesheet" href="https://fonts.googleapis.com/css2?family=Source+Sans+3:wght@400;600;700;900&display=swap">
<style>
  :root {
    --bg: #ecebe8;
    --paper: #ffffff;
    --brand-red: #f40b0b;
    --name-red: #a3161a;
    --ink: #1a1a1a;
    --text: #4a4a4a;
    --rule: #9a9a9a;
    --band: #0c0c0c;
    --map-light: #e3dcc8;
    --map-dark: #c9bf9f;
  }
  * { margin: 0; padding: 0; box-sizing: border-box; }
  html, body { width: 1200px; height: 987px; overflow: hidden; }
  body {
    background: var(--bg);
    font-family: "Source Sans 3", sans-serif;
    position: relative;
  }
  .card {
    position: absolute;
    width: 615px;
    height: 351px;
    overflow: hidden;
    box-shadow: 0 2px 6px rgba(0,0,0,.18);
  }
  .card-front { left: 293px; top: 130px; background: var(--paper); }
  .card-back { left: 292px; top: 506px; background: var(--brand-red); color: #fff; }

  /* front */
  .front-brand {
    position: absolute; right: 40px; top: 62px;
    display: flex; align-items: center; gap: 10px;
    font-weight: 900; font-size: 38px; line-height: 1; letter-spacing: 1px;
    color: var(--ink); text-transform: uppercase;
  }
  .brand-mark { width: 18px; height: 18px; background: var(--brand-red); flex: none; }
  .person-name {
    position: absolute; left: 39px; top: 175px;
    font-size: 22px; font-weight: 600; color: var(--name-red); letter-spacing: .3px;
  }
  .person-title {
    position: absolute; left: 39px; top: 203px;
    font-size: 16px; color: var(--ink);
  }
  .divider {
    position: absolute; left: 39px; top: 232px; width: 538px;
    border-top: 1px solid var(--rule);
  }
  .contact-list {
    position: absolute; left: 39px; top: 247px; list-style: none;
    font-size: 16.5px; color: var(--text); line-height: 23px;
  }
  .contact-list li { display: flex; align-items: center; gap: 8px; }
  .contact-list svg { width: 15px; height: 15px; fill: var(--name-red); flex: none; }
  .address {
    position: absolute; right: 38px; top: 247px; text-align: right;
    font-size: 16.5px; color: var(--text); line-height: 23px; font-style: normal;
  }
  .bottom-band { position: absolute; left: 0; bottom: 0; width: 615px; height: 40px; }
  .website {
    position: absolute; right: 33px; bottom: 10px;
    font-size: 16.5px; color: #fff; letter-spacing: .2px;
  }

  /* back */
  .back-brand {
    position: absolute; left: 36px; top: 46px;
    display: flex; align-items: center; gap: 9px;
    font-weight: 900; font-size: 28px; line-height: 1; letter-spacing: .8px;
    text-transform: uppercase; color: #fff;
  }
  .back-brand .brand-mark { background: #fff; width: 13px; height: 13px; }
  .service-list {
    position: absolute; left: 33px; top: 111px; list-style: none;
    font-size: 17px; font-weight: 700; line-height: 23.5px;
  }
  .service-list li::before { content: "•"; margin-right: 8px; }
  .social {
    position: absolute; left: 32px; top: 194px;
    display: flex; align-items: center; gap: 7px;
    font-size: 17px; font-weight: 700;
  }
  .social-dot { width: 20px; height: 20px; border-radius: 50%; background: #fff; }
  .store-name {
    position: absolute; left: 32px; top: 230px;
    font-size: 24px; font-weight: 700;
  }
  .store-location {
    position: absolute; left: 32px; top: 260px;
    font-size: 18px; font-weight: 700;
  }
  .membership {
    position: absolute; left: 32px; top: 295px;
    display: flex; align-items: flex-end; font-size: 16.5px;
  }
  .membership-line {
    display: inline-block; width: 150px; border-bottom: 1px solid #fff;
    margin-left: 2px; margin-bottom: 4px;
  }
  .location-map {
    position: absolute; left: 306px; top: 36px; width: 281px; height: 283px;
    border-radius: 9px;
    background: radial-gradient(circle at 40% 55%, var(--map-light), var(--map-dark));
  }
</style>
</head>
<body>
  <section class="card card-front" aria-label="Business card front">
    <div class="front-brand"><span class="brand-mark"></span>Vital Harbor</div>
    <h1 class="person-name">DANIEL REYES</h1>
    <p class="person-title">CEO/Founder</p>
    <div class="divider"></div>
    <ul class="contact-list">
      <li><svg viewBox="0 0 24 24" aria-hidden="true"><path d="M6.6 10.8a15.5 15.5 0 0 0 6.6 6.6l2.2-2.2c.3-.3.7-.4 1-.2 1.1.4 2.3.6 3.6.6.6 0 1 .4 1 1V20c0 .6-.4 1-1 1A17 17 0 0 1 3 4c0-.6.4-1 1-1h3.5c.6 0 1 .4 1 1 0 1.3.2 2.5.6 3.6.1.3 0 .7-.2 1z"/></svg>(281)-555-0147</li>
      <li><svg viewBox="0 0 24 24" aria-hidden="true"><path d="M2 5h20v14H2z" fill="var(--name-red)"/><path d="M2 5l10 7 10-7" fill="none" stroke="#fff" stroke-width="1.6"/></svg>daniel@myvitalharbor.com</li>
    </ul>
    <address class="address">27591 Maple Crest Parkway<br>Mapleview, KS 77592</address>
    <svg class="bottom-band" viewBox="0 0 615 40" aria-hidden="true">
      <polygon points="0,14 325,14 318,26 0,26" fill="var(--brand-red)"/>
      <polygon points="0,26 318,26 316,29 0,29" fill="var(--band)"/>
      <polygon points="339,0 615,0 615,40 315,40" fill="var(--band)"/>
    </svg>
    <span class="website">www.myvitalharbor.com</span>
  </section>

  <section class="card card-back" aria-label="Business card back">
    <div class="back-brand"><span class="brand-mark"></span>Vital Harbor</div>
    <ul class="service-list">
      <li>Sports Nutrition</li>
      <li>Vitamins/Herbs</li>
      <li>Weight Loss</li>
    </ul>
    <div class="social"><span class="social-dot"></span>@VHMapleview</div>
    <h2 class="store-name">The Mapleview Store</h2>
    <p class="store-location">Maple Creek Shopping Center</p>
    <p class="membership">Membership:<span class="membership-line"></span></p>
    <div class="location-map" role="img" aria-label="Street map showing the store location in the shopping center near the freeway"></div>
  </section>
</body>
</html>
```